Medic Harbour

Our product is a subscription-based website for doctors and medical practices. It allows contract-based doctors (locums) to book jobs with medical practices and to organise their own finances (invoicing, pension, etc). Also, it allows medical practices to post jobs, and book locums.

We need a website design that looks clean and professional. It should look easy-to-use and friendly, which will encourage users to sign up as they'll hopefully think using the system will also be simple and friendly.

As well as the homepage, we need a design for the logged-in view. This is very different to the website but equally important. It needs to be very functional. Much more like an application and less like a website.

PLEASE SUBMIT BOTH WEBSITE HOMEPAGE DESIGN AND APPLICATION DASHBOARD DESIGN.

The application is built and we already have a user interface (linked below) so we're not looking for a designer to decide what is on these pages - we already have that. We're ONLY asking for visual design. Please just make the content we have look good. You may move parts of the content around a small amount but the functionality is very much signed off now so it's only visual styling that we need addressed.

Please base the branding around the current logo, which can't be changed. You can get the logo as an EPS here : http://clients.plumowl.co.uk/medicharbour/design/logo-green.eps

Here is a link to the current design for the website, and for the application dashboard:
http://clients.plumowl.co.uk/medicharbour/design/

Also, here is a video we've had made which might help you with the brand:
http://clipvane.com/81527364
Updates

Just in case it isn't clear, the video (linked in the main brief) is an essential part of the website homepage.

Reason: We need to spend some time looking over these designs and might ask for a few amendments to one or two in the next few days. Thanks.

Target Market(s)

Doctors and medical practices

Industry/Entity Type

Medical

Requirements
Must have
• It must have all the features that are in the linked designs - homepage and dashboard.

```html
<!DOCTYPE html>
<html lang="en">
<head>
<meta charset="utf-8">
<title>Medic Harbour – A network connecting locums with employers</title>
<link rel="stylesheet" href="https://fonts.googleapis.com/css2?family=Ubuntu:wght@400;500;700&family=Open+Sans:wght@400;600;700&display=swap">
<style>
:root{
  --navy:#1c3c57;
  --ink:#3a4650;
  --muted:#5d6b74;
  --brand-blue:#1d8ac4;
  --brand-green:#6cab23;
  --header-top:#e9f7fc;
  --header-bottom:#d5eef8;
  --nav-top:#d9f0a4;
  --nav-bottom:#a6d35a;
  --hero-top:#4d9c1c;
  --hero-mid:#80c23b;
  --hero-bottom:#aedb6a;
  --cta-top:#ffc53b;
  --cta-bottom:#f39a0b;
  --btn-blue-top:#36a7e2;
  --btn-blue-bottom:#1570ae;
  --btn-navy:#1d5275;
  --grey-top:#ffffff;
  --grey-bottom:#e6e8ea;
  --band:#e6f6fd;
  --band-line:#b9e0f1;
  --bubble:#e3f7c9;
  --footer:#d6f1fc;
  --white:#ffffff;
  --step:#8a7f62;
  --step-green:#7cbe31;
}
*{box-sizing:border-box;margin:0;padding:0}
html,body{width:1200px;height:2271px;overflow:hidden}
body{position:relative;font-family:"Open Sans",Arial,sans-serif;color:var(--ink);background:var(--white)}
.abs{position:absolute}

/* Header */
.site-header{position:absolute;left:0;top:0;width:1200px;height:136px;background:linear-gradient(var(--header-top),var(--header-bottom))}
.brand{position:absolute;left:145px;top:32px;display:flex;align-items:center;gap:14px}
.brand-mark{width:78px;height:78px;border-radius:50%;background:var(--brand-blue)}
.brand-name{font-family:"Ubuntu",sans-serif;font-weight:700;font-size:31px;line-height:32px;color:var(--brand-blue);letter-spacing:.5px;width:170px}
.signout-tab{position:absolute;left:905px;top:0;width:152px;height:30px;background:linear-gradient(#2a8fc9,#175f92);border-radius:0 0 10px 10px;color:#fff;font:700 12px "Open Sans",sans-serif;text-align:center;line-height:30px}
.user-name{position:absolute;left:905px;top:44px;width:152px;text-align:center;font:600 14px "Open Sans",sans-serif;color:var(--navy)}
.dashboard-btn{position:absolute;left:895px;top:78px;width:166px;height:36px;border-radius:18px;background:linear-gradient(var(--btn-blue-top),var(--btn-blue-bottom));color:#fff;font:700 13px "Open Sans",sans-serif;display:flex;align-items:center;justify-content:center;gap:7px;box-shadow:0 2px 3px rgba(0,0,0,.2)}

/* Nav */
.main-nav{position:absolute;left:0;top:136px;width:1200px;height:38px;background:linear-gradient(var(--nav-top),var(--nav-bottom));border-bottom:1px solid #7fb33a}
.main-nav a{position:absolute;top:0;height:38px;line-height:38px;transform:translateX(-50%);font:700 14px "Open Sans",sans-serif;color:var(--navy);text-decoration:none}
.main-nav a.current{top:6px;height:26px;line-height:26px;padding:0 16px;background:#fff;border-radius:13px;box-shadow:0 1px 2px rgba(0,0,0,.25)}

/* Hero */
.hero{position:absolute;left:0;top:175px;width:1200px;height:351px;background:radial-gradient(ellipse at 70% 30%,var(--hero-mid),transparent 70%),linear-gradient(var(--hero-top),var(--hero-mid) 60%,var(--hero-bottom))}
.video{position:absolute;left:151px;top:30px;width:474px;height:280px;border:3px solid #dfe6ea;border-radius:4px;background:radial-gradient(circle at 50% 45%,#eaf7fd,#7ec4e3 75%,#4fa2c9);box-shadow:0 4px 10px rgba(0,0,0,.3)}
.video-title{position:absolute;left:8px;top:10px;display:flex;gap:6px}
.video-thumb{width:58px;height:48px;background:#fff}
.video-title p{font:600 16px "Open Sans",sans-serif;color:#7fd3ff;background:rgba(20,30,40,.8);padding:2px 6px;height:26px}
.video-title small{display:block;font-size:10px;color:#ccc;margin-top:6px}
.video-brand{position:absolute;left:90px;top:98px;display:flex;align-items:center;gap:14px}
.video-brand .brand-mark{width:86px;height:86px}
.video-brand .brand-name{font-size:36px;line-height:36px;width:200px}
.player-bar{position:absolute;left:8px;bottom:8px;right:8px;height:36px;display:flex;align-items:center;gap:8px}
.play{width:52px;height:36px;border-radius:4px;background:rgba(20,30,40,.85);display:flex;align-items:center;justify-content:center}
.track{flex:1;height:36px;border-radius:4px;background:rgba(20,30,40,.85);display:flex;align-items:center;padding:0 10px;gap:10px;color:#fff;font:700 12px "Open Sans",sans-serif}
.track .line{flex:1;height:8px;background:#4b5962}
.hero-title{position:absolute;left:666px;top:27px;font:500 35px/42px "Ubuntu",sans-serif;color:#fff;text-shadow:0 1px 2px rgba(0,0,0,.25)}
.hero-title strong{font-weight:700}
.hero-points{position:absolute;left:666px;top:120px;list-style:none}
.hero-points li{font:italic 400 18px/33px "Open Sans",sans-serif;color:#fff;display:flex;align-items:center;gap:12px}
.cta{position:absolute;left:672px;top:264px;width:326px;height:57px;border-radius:10px;background:linear-gradient(var(--cta-top),var(--cta-bottom));border:3px solid #d8820a;color:#fff;font:500 22px "Ubuntu",sans-serif;text-align:center;line-height:51px;text-shadow:0 1px 1px rgba(0,0,0,.3)}

/* Audiences */
.audiences{position:absolute;left:0;top:526px;width:1200px;height:449px;background:linear-gradient(var(--grey-top) 0,#f4f5f6 60%,var(--grey-bottom))}
.audience{position:absolute;top:30px;width:420px}
.audience h2{font:700 23px "Ubuntu",sans-serif;color:var(--navy)}
.audience .lede{font-size:14px;color:var(--navy);margin-top:4px}
.steps{list-style:none;margin-top:20px}
.steps li{position:relative;padding-left:30px;margin-bottom:20px}
.steps .num{position:absolute;left:0;top:0;width:22px;height:22px;border-radius:50%;background:var(--step);color:#fff;font:700 12px/22px "Open Sans",sans-serif;text-align:center}
.steps h3{font:700 15px "Open Sans",sans-serif;color:var(--navy)}
.steps p{font-size:13px;line-height:19px;color:var(--muted);margin-top:2px}
.aud-actions{display:flex;align-items:center;gap:18px;margin-left:30px}
.btn-navy{width:66px;height:36px;border-radius:5px;background:var(--btn-navy);color:#fff;font:600 14px/36px "Open Sans",sans-serif;text-align:center}
.more{font:700 11px/15px "Open Sans",sans-serif;color:var(--navy);width:200px}

/* How it works */
.how{position:absolute;left:0;top:975px;width:1200px;height:98px;background:var(--band);border-top:3px solid var(--band-line);border-bottom:3px solid var(--band-line)}
.how h2{position:absolute;left:138px;top:14px;font:500 18px "Ubuntu",sans-serif;color:var(--navy);letter-spacing:1px}
.how-step{position:absolute;top:50px;display:flex;align-items:center;gap:10px;font:600 13px "Open Sans",sans-serif;color:var(--navy)}
.how-step .num{width:28px;height:28px;border-radius:50%;background:var(--step-green);color:#fff;font:700 14px/28px "Open Sans",sans-serif;text-align:center;border:2px solid #e6f3d2}

/* Sign up */
.signup-title{position:absolute;left:0;top:1110px;width:1200px;text-align:center;font:400 28px "Ubuntu",sans-serif;color:#333}
.signup-form{position:absolute;left:142px;top:1200px;width:440px;font-size:14px;color:#333}
.radio-row{display:flex;align-items:center;gap:6px}
.radio{width:13px;height:13px;border-radius:50%;border:1px solid #888;display:inline-block;background:#fff}
.radio.on{background:radial-gradient(#2a6fb3 35%,#fff 40%)}
.field{position:absolute;width:210px}
.field label{display:block;font-size:14px;margin-bottom:8px}
.field span{display:block;height:32px;border:1px solid #b7bcc0;background:#fff}
.agree{position:absolute;left:0;top:186px;display:flex;align-items:center;gap:7px;font-size:14px}
.agree i{width:12px;height:12px;border:1px solid #888;display:inline-block}
.agree a{color:#1d75b4;text-decoration:none}
.btn-green{position:absolute;left:0;top:226px;width:76px;height:36px;border-radius:5px;background:linear-gradient(#8dc84a,#5d9a22);color:#fff;font:600 14px/36px "Open Sans",sans-serif;text-align:center}
.team-photo{position:absolute;left:558px;top:1164px;width:512px;height:304px;background:radial-gradient(ellipse at 50% 45%,#dfe8ee 0,#eef3f6 50%,#fff 75%)}

/* Press */
.press{position:absolute;left:0;top:1470px;width:1200px;height:451px;background:linear-gradient(#fff 0,#fff 55%,var(--grey-bottom))}
.quote{position:absolute;top:44px;width:246px;height:246px;border-radius:50%;background:var(--bubble);padding:62px 40px 0;text-align:center;font-size:14px;line-height:23px;color:#333}
.quote::before{content:"\201C";position:absolute;left:28px;top:6px;font:700 72px Georgia,serif;color:#fff}
.quote::after{content:"";position:absolute;right:38px;bottom:-14px;border-style:solid;border-width:30px 0 0 30px;border-color:var(--bubble) transparent transparent transparent;transform:rotate(12deg)}
.outlet{position:absolute;top:300px;width:246px;text-align:center;font:700 28px "Ubuntu",sans-serif;color:#1f2a33}

/* Footer */
.site-footer{position:absolute;left:0;top:1921px;width:1200px;height:350px;background:var(--footer);border-top:6px solid #a9d6ea}
.testimonial{position:absolute;top:40px;display:flex;gap:14px}
.avatar{width:40px;height:40px;border-radius:4px;background:#f1c79a}
.testimonial p{background:#fff;border-radius:6px;padding:8px 12px;font-size:13px;line-height:21px;color:#445;width:380px}
.cite{position:absolute;top:112px;font:italic 11px "Open Sans",sans-serif;color:#445;text-align:right;width:230px}
.footer-rule{position:absolute;left:138px;top:152px;width:924px;height:1px;background:#b6dcea}
.footer-nav{position:absolute;left:0;top:176px;width:1200px;text-align:center;font-size:12px}
.footer-nav a{color:var(--navy);text-decoration:none;margin:0 18px}
.help{position:absolute;left:0;top:240px;width:1200px;text-align:center;font-size:12px;color:var(--navy)}
.help strong{font-weight:700}
.legal{position:absolute;left:0;top:280px;width:1200px;text-align:center;font-size:12px;line-height:23px;color:var(--navy)}
</style>
</head>
<body>

<header class="site-header">
  <div class="brand"><span class="brand-mark"></span><span class="brand-name">MEDIC HARBOUR</span></div>
  <div class="signout-tab">SIGN OUT</div>
  <div class="user-name">Mrs. Helen Marsh</div>
  <div class="dashboard-btn">Go to Dashboard
    <svg width="13" height="13" viewBox="0 0 13 13"><circle cx="6.5" cy="6.5" r="5.5" fill="none" stroke="#fff" stroke-width="1.5"/><path d="M5 4l2.5 2.5L5 9" fill="none" stroke="#fff" stroke-width="1.5"/></svg>
  </div>
</header>

<nav class="main-nav">
  <a class="current" style="left:208px">HOME</a>
  <a style="left:324px">LOCUMS</a>
  <a style="left:458px">EMPLOYERS</a>
  <a style="left:592px">PRICING</a>
  <a style="left:716px">ABOUT US</a>
  <a style="left:835px">FAQ'S</a>
  <a style="left:965px">CONTACT US</a>
</nav>

<section class="hero">
  <div class="video" role="img" aria-label="Medic Harbour introduction video">
    <div class="video-title"><span class="video-thumb"></span><div><p>Medic Harbour</p><small>from Reelnest.com</small></div></div>
    <div class="video-brand"><span class="brand-mark"></span><span class="brand-name">MEDIC HARBOUR</span></div>
    <div class="player-bar">
      <div class="play"><svg width="16" height="18" viewBox="0 0 16 18"><path d="M2 1l13 8-13 8z" fill="#fff"/></svg></div>
      <div class="track"><span>01:48</span><span class="line"></span><span>HD</span><span>clipvane</span></div>
    </div>
  </div>
  <h1 class="hero-title">A Network for connection<br><strong>LOCUMS</strong> with employers.</h1>
  <ul class="hero-points">
    <li><svg width="14" height="10" viewBox="0 0 14 10"><path d="M0 5h12M8 1l4 4-4 4" fill="none" stroke="#fff" stroke-width="1.6"/></svg>Better Connectivity</li>
    <li><svg width="14" height="10" viewBox="0 0 14 10"><path d="M0 5h12M8 1l4 4-4 4" fill="none" stroke="#fff" stroke-width="1.6"/></svg>More Choice</li>
    <li><svg width="14" height="10" viewBox="0 0 14 10"><path d="M0 5h12M8 1l4 4-4 4" fill="none" stroke="#fff" stroke-width="1.6"/></svg>Less Paperwork</li>
    <li><svg width="14" height="10" viewBox="0 0 14 10"><path d="M0 5h12M8 1l4 4-4 4" fill="none" stroke="#fff" stroke-width="1.6"/></svg>Lower Costs</li>
  </ul>
  <div class="cta">Sign up for free - Try us out</div>
</section>

<section class="audiences">
  <div class="audience" style="left:142px">
    <h2>GP LOCUMS</h2>
    <p class="lede">The complete platform to organise your locum life</p>
    <ol class="steps">
      <li><span class="num">1</span><h3>Find Jobs</h3><p>Search, apply &amp; get invited for a wide selection<br>of jobs from pratices &amp; agencies</p></li>
      <li><span class="num">2</span><h3>Do your locum admin easily online</h3><p>Profile, dairy management, invoicing,pension forms,<br>finances, tax returns</p></li>
      <li><span class="num">3</span><h3>Create &amp; Grow your “Employer Network”</h3><p>Create your online profile &amp; connect with your own<br>network of employers allowing you to automatically<br>fill jobs</p></li>
    </ol>
    <div class="aud-actions"><span class="btn-navy">Sign up</span><span class="more">More about Medic Harbour<br>for locums</span></div>
  </div>
  <div class="audience" style="left:672px">
    <h2>EMPLOYERS</h2>
    <p class="lede">One-stop solution for your locum needs</p>
    <ol class="steps">
      <li><span class="num">1</span><h3>Find locums</h3><p>Post your locum requirements. Search &amp; employ<br>the right locums via your e-booking system</p></li>
      <li><span class="num">2</span><h3>Do your locum admin easily online</h3><p>Profile, locum rota management, pre-employment<br>checks, locum market statistics</p></li>
      <li><span class="num">3</span><h3>Create &amp; grow your “Local Network”</h3><p>Create your online profile &amp; connect with your own<br>network of locums allowing them to automatically<br>fill jobs</p></li>
    </ol>
    <div class="aud-actions"><span class="btn-navy">Sign up</span><span class="more">More about Medic Harbour<br>for employers</span></div>
  </div>
</section>

<section class="how">
  <h2>HOW IT WORKS</h2>
  <div class="how-step" style="left:140px"><span class="num">1</span>“The Network” for locums &amp; employers</div>
  <div class="how-step" style="left:540px"><span class="num">2</span>Save time and cost</div>
  <div class="how-step" style="left:808px"><span class="num">3</span>Try it free now</div>
</section>

<h2 class="signup-title">Try it now with just an email address, GMC number and password!</h2>
<svg class="abs" style="left:410px;top:1148px" width="150" height="90" viewBox="0 0 150 90"><path d="M12 2C0 30 40 40 90 38s50 20 46 44" fill="none" stroke="#333" stroke-width="1.5" stroke-dasharray="3 4"/><path d="M130 76l6 8 5-9" fill="none" stroke="#333" stroke-width="1.5"/></svg>
<form class="signup-form">
  <div class="radio-row">I am <span class="radio on"></span> a locum <span class="radio"></span> an employer</div>
  <div class="field" style="left:0;top:46px"><label>Email</label><span></span></div>
  <div class="field" style="left:222px;top:46px"><label>GMC Number</label><span></span></div>
  <div class="field" style="left:0;top:112px"><label>Password</label><span></span></div>
  <div class="field" style="left:222px;top:112px"><label>Confirm Passowrd</label><span></span></div>
  <div class="agree"><i></i>I agree to the <a>terms of services</a> and <a>privacy policy</a></div>
  <div class="btn-green">Sign up</div>
</form>
<div class="team-photo" role="img" aria-label="Photograph of a team of smiling doctors in white coats"></div>

<section class="press">
  <blockquote class="quote" style="left:165px">Lorem Ipsum is simply dummy text of the printing and typesetting industry. Lorem Ipsum has been the industry's dummy text.</blockquote>
  <blockquote class="quote" style="left:479px">Lorem Ipsum is simply dummy text of the printing and typesetting industry. Lorem Ipsum has been the industry's dummy text.</blockquote>
  <blockquote class="quote" style="left:789px">Lorem Ipsum is simply dummy text of the printing and typesetting industry. Lorem Ipsum has been the industry's dummy text.</blockquote>
  <p class="outlet" style="left:165px">courier.co.uk</p>
  <p class="outlet" style="left:479px">Evening Wire</p>
  <p class="outlet" style="left:789px">Herald Times</p>
</section>

<footer class="site-footer">
  <div class="testimonial" style="left:142px"><span class="avatar" role="img" aria-label="Locum avatar"></span><p>So easy to set up. Five minutes adn you're in.<br>And it does all the boring admin stuff that I hate.</p></div>
  <div class="cite" style="left:320px">Name of person, Lacum</div>
  <div class="testimonial" style="left:648px"><span class="avatar" role="img" aria-label="Practice avatar"></span><p>As a pratice, it's great to be able to find locums<br>quickly &amp; easily. No more timeconsuming...</p></div>
  <div class="cite" style="left:824px">Blah Medical Centre</div>
  <div class="footer-rule"></div>
  <nav class="footer-nav"><a>Home</a><a>Locums</a><a>Employers</a><a>About Us</a><a>FAQ's</a><a>Contact Us</a></nav>
  <p class="help">We're here to help: <strong>support@medicharbour.co.uk</strong></p>
  <p class="legal">Copyright © 2013 Medic Harbour Ltd. All Rights Reserved.<br>Registered in England no. 08421937</p>
</footer>

</body>
</html>
```